Outdoor banner - allegorical car (float) on Gay Pride

We need a graphics for advertising banner promoting web project www.velvorio.net
Approximate size 120x40inch (3x1meters) - Therefore, it is required vector graphics, any embedded bitmaps in high resolution.

We launching new social network and city guide application for Prague visitors.
Keywords for poster are: city, Prague, traveling, rainbow, party, colors, holiday,..
It must contain the dominant text "VELVORIO.NET".
Banner will be placed on an float (allegorical car) in the parade Tamsel Color March 2014. And this banner will be the dominant car graphics.

- modern party look
- it should be understood that it is the queer(gay) web :)
- appropriate use of rainbow colors( or elements) in the graphics
- is possible to use silhouette of Prague

update:
- preferred is a vector graphics (vector elements)
- with regard to the size of the banner is not suitable the one big bitmap photo
- banner will be horizontal
Updates

update: - preferred is a vector graphics (vector elements) - with regard to the size of the banner is not suitable the one big bitmap photo

Target Market(s)

Prague visitors ..looking for entertainment., services..

Industry/Entity Type

Advertising

Requirements
Must have
• dominant text "VELVORIO.NET"
rainbow colors( or elements) in the graphics
vector graphics for large format printing

```html
<!DOCTYPE html>
<html lang="en">
<head>
<meta charset="utf-8">
<title>VELVORIO.NET – Enjoy the best of Tamsel</title>
<link rel="stylesheet" href="https://fonts.googleapis.com/css2?family=Bebas+Neue&display=swap">
<style>
  :root {
    --red: #d8242a;
    --orange: #ef7d1f;
    --yellow: #f3dc1e;
    --green: #1f8a3a;
    --blue: #22399a;
    --purple: #5b2a86;
    --fold-dark: rgba(0, 0, 0, 0.38);
    --fold-light: rgba(255, 255, 255, 0.16);
    --title: #ffffff;
    --tagline: #ece3cf;
  }
  html, body {
    margin: 0;
    padding: 0;
    overflow: hidden;
    background: #ffffff;
  }
  .banner {
    position: relative;
    width: 1200px;
    height: 400px;
    overflow: hidden;
  }
  .banner-art {
    display: block;
    width: 1200px;
    height: 400px;
  }
  .flag-band { shape-rendering: crispEdges; }
  .band-red { fill: var(--red); }
  .band-orange { fill: var(--orange); }
  .band-yellow { fill: var(--yellow); }
  .band-green { fill: var(--green); }
  .band-blue { fill: var(--blue); }
  .band-purple { fill: var(--purple); }
  .stop-dark { stop-color: var(--fold-dark); }
  .stop-light { stop-color: var(--fold-light); }
  .stop-clear { stop-color: rgba(0, 0, 0, 0); }
  .stop-city-a { stop-color: rgba(40, 35, 30, 0.40); }
  .stop-city-b { stop-color: rgba(40, 40, 35, 0.22); }
  .stop-city-c { stop-color: rgba(30, 30, 40, 0.36); }
  .site-name {
    font-family: "Bebas Neue", "Arial Narrow", sans-serif;
    font-size: 200px;
    fill: var(--title);
  }
  .tagline {
    font-family: "Bebas Neue", "Arial Narrow", sans-serif;
    font-size: 94px;
    fill: var(--tagline);
  }
</style>
</head>
<body>
<main class="banner">
  <svg class="banner-art" viewBox="0 0 1200 400" xmlns="http://www.w3.org/2000/svg">
    <defs>
      <linearGradient id="flag-folds" x1="0" y1="0" x2="1" y2="0.2">
        <stop offset="0" class="stop-dark"/>
        <stop offset="0.12" class="stop-clear"/>
        <stop offset="0.28" class="stop-light"/>
        <stop offset="0.45" class="stop-dark"/>
        <stop offset="0.62" class="stop-clear"/>
        <stop offset="0.78" class="stop-light"/>
        <stop offset="0.92" class="stop-dark"/>
        <stop offset="1" class="stop-clear"/>
      </linearGradient>
      <linearGradient id="city-wash" x1="0" y1="0" x2="1" y2="0">
        <stop offset="0" class="stop-city-a"/>
        <stop offset="0.5" class="stop-city-b"/>
        <stop offset="1" class="stop-city-c"/>
      </linearGradient>
    </defs>

    <g class="rainbow-flag">
      <rect class="flag-band band-red" x="0" y="0" width="1200" height="68"/>
      <rect class="flag-band band-orange" x="0" y="68" width="1200" height="66"/>
      <rect class="flag-band band-yellow" x="0" y="134" width="1200" height="64"/>
      <rect class="flag-band band-green" x="0" y="198" width="1200" height="68"/>
      <rect class="flag-band band-blue" x="0" y="266" width="1200" height="68"/>
      <rect class="flag-band band-purple" x="0" y="334" width="1200" height="66"/>
      <rect class="flag-folds" x="0" y="0" width="1200" height="400" fill="url(#flag-folds)"/>
    </g>

    <rect class="city-skyline" role="img" aria-label="Faded photograph of old city rooftops, domes and spires blended into the flag"
          x="0" y="0" width="1200" height="400" fill="url(#city-wash)"/>

    <text class="site-name" x="600" y="192" text-anchor="middle"
          textLength="1120" lengthAdjust="spacingAndGlyphs">VELVORIO.NET</text>

    <text class="tagline" x="604" y="330" text-anchor="middle"
          textLength="760" lengthAdjust="spacingAndGlyphs">ENJOY THE BEST OF TAMSEL</text>
  </svg>
</main>
</body>
</html>
```